Business Card for beauty technology startup

Design Glowmi Business Card for a Beauty, based on the website identity and colors (https://www.glowmi-example.com).
Glowmi is a beauty tech startup that gathers helpful product info for beauty lovers and consumers (such as availability on stores, price range and product reviews) for makeup products. The card design must be young, colorful but clean, and very modern.

Target Market(s)

woman, 15-35

Industry/Entity Type

Cosmetics

Contact Information for Business Card

Full Name, address, phone

Font styles to use
Other font styles liked:
• Advent Pro

Colors
e34297
86cfc6
ffffff
5c5c5c
e8e8e8
e667a6
b2b2b2

Requirements
Must have
• One full colored side with a creative design and another with card info
• Use Color palette: #95C5C5 and/or #D38AA5
• Use fonts: Advent Pro
• Use website identity: https://www.glowmi-example.com
Nice to have
• If needed extra font: Roboto

```html
<!DOCTYPE html>
<html lang="en">
<head>
<meta charset="utf-8">
<title>Glowmi Business Card</title>
<link href="https://fonts.googleapis.com/css2?family=Advent+Pro:wght@300;400;600;700&display=swap" rel="stylesheet">
<style>
  :root {
    --magenta: #e34297;
    --pink: #e667a6;
    --pink-bright: #ff6fb9;
    --teal: #86cfc6;
    --white: #ffffff;
    --ink: #1e1a1a;
    --grey: #5c5c5c;
    --line: #b2b2b2;
    --stage: #e8e8e8;
  }
  * { box-sizing: border-box; margin: 0; padding: 0; }
  html, body { width: 1200px; height: 1200px; overflow: hidden; }
  body {
    background: var(--stage);
    font-family: "Advent Pro", sans-serif;
    position: relative;
  }
  .card {
    position: absolute;
    left: 150px;
    width: 900px;
    height: 514px;
    overflow: hidden;
    box-shadow: 0 10px 30px rgba(0,0,0,.15);
  }
  /* Info side */
  .card--info { top: 50px; background: var(--white); }
  .info__brand {
    position: absolute;
    left: 40px; top: 100px;
    width: 360px;
    display: flex; flex-direction: column; align-items: center; gap: 14px;
  }
  .info__brand-ring {
    width: 96px; height: 96px; border-radius: 50%;
    border: 5px solid var(--ink);
  }
  .info__brand-name {
    font-size: 68px; font-weight: 300; letter-spacing: 10px;
    color: var(--ink); text-transform: uppercase; line-height: 1;
  }
  .info__divider {
    position: absolute; left: 420px; top: 70px;
    width: 2px; height: 330px; background: var(--line);
  }
  .info__details { position: absolute; left: 460px; top: 90px; color: var(--grey); }
  .info__name {
    display: flex; align-items: center; gap: 10px;
    font-size: 44px; font-weight: 700; color: var(--magenta);
    text-transform: uppercase; letter-spacing: 1px; line-height: 1;
  }
  .info__title { font-size: 28px; margin: 4px 0 26px 48px; }
  .info__row {
    display: flex; align-items: flex-start; gap: 14px;
    font-size: 28px; line-height: 1.25; margin-bottom: 8px;
  }
  .info__row svg, .info__name svg { flex: none; margin-top: 4px; }
  .info__band {
    position: absolute; left: 0; bottom: 0; width: 100%; height: 64px;
    display: flex;
  }
  .info__band span:nth-child(1) { flex: 0 0 26%; background: var(--teal); }
  .info__band span:nth-child(2) { flex: 0 0 38%; background: var(--magenta); }
  .info__band span:nth-child(3) { flex: 1; background: var(--pink); }
  /* Brand side */
  .card--brand {
    top: 636px;
    background: linear-gradient(120deg, var(--magenta) 0%, var(--pink-bright) 60%, #ff86c6 100%);
  }
  .brand__bubbles { position: absolute; inset: 0; }
  .brand__logo {
    position: absolute; left: 110px; top: 110px;
    display: flex; align-items: center; gap: 24px;
  }
  .brand__ring {
    width: 150px; height: 150px; border-radius: 50%;
    border: 6px solid var(--white);
  }
  .brand__name { font-size: 88px; font-weight: 600; color: var(--white); line-height: 1; }
  .brand__url {
    position: absolute; left: 110px; bottom: 110px;
    font-size: 34px; color: var(--white);
  }
</style>
</head>
<body>
  <section class="card card--info" aria-label="Card info side">
    <div class="info__brand">
      <span class="info__brand-ring"></span>
      <span class="info__brand-name">Glowmi</span>
    </div>
    <div class="info__divider"></div>
    <div class="info__details">
      <p class="info__name">
        <svg width="34" height="34" viewBox="0 0 24 24" fill="var(--magenta)"><circle cx="12" cy="7" r="5"/><path d="M2 23c0-6 4.5-9 10-9s10 3 10 9z"/></svg>
        Mara Lind
      </p>
      <p class="info__title">Director</p>
      <p class="info__row">
        <svg width="26" height="26" viewBox="0 0 24 24" fill="var(--magenta)"><path d="M6.6 10.8a15 15 0 0 0 6.6 6.6l2.2-2.2a1 1 0 0 1 1-.25 11.4 11.4 0 0 0 3.6.57 1 1 0 0 1 1 1V20a1 1 0 0 1-1 1A17 17 0 0 1 3 4a1 1 0 0 1 1-1h3.5a1 1 0 0 1 1 1c0 1.25.2 2.45.57 3.6a1 1 0 0 1-.25 1z"/></svg>
        1-555-010-2030
      </p>
      <p class="info__row">
        <svg width="26" height="26" viewBox="0 0 24 24" fill="none" stroke="var(--magenta)" stroke-width="2"><circle cx="12" cy="12" r="10"/><path d="M2 12h20M12 2a15 15 0 0 1 0 20M12 2a15 15 0 0 0 0 20"/></svg>
        www.glowmi-example.com
      </p>
      <p class="info__row">
        <svg width="26" height="26" viewBox="0 0 24 24" fill="var(--magenta)"><path d="M12 2a7 7 0 0 0-7 7c0 5 7 13 7 13s7-8 7-13a7 7 0 0 0-7-7zm0 9.5A2.5 2.5 0 1 1 12 6.5a2.5 2.5 0 0 1 0 5z"/></svg>
        <span>Rosewood City<br>Examplia Land</span>
      </p>
    </div>
    <div class="info__band"><span></span><span></span><span></span></div>
  </section>

  <section class="card card--brand" aria-label="Card brand side">
    <svg class="brand__bubbles" width="900" height="514" viewBox="0 0 900 514" aria-hidden="true">
      <circle cx="760" cy="180" r="180" fill="#ffffff" opacity=".16"/>
      <circle cx="700" cy="560" r="260" fill="#ffffff" opacity=".16"/>
      <circle cx="440" cy="640" r="220" fill="#ffffff" opacity=".12"/>
    </svg>
    <div class="brand__logo">
      <span class="brand__ring"></span>
      <span class="brand__name">Glowmi</span>
    </div>
    <p class="brand__url">www.glowmi-example.com</p>
  </section>
</body>
</html>
```